`Beneath the Quiet Copper Fern` by Peter R Dunmore

Hi, I would like a paperback book cover which potentially has the following......
Photograph of a canal, a lock, a narrow-boat, some pretty scenery (Summer/Autumn) a magpie, a photobomb of a black and white cats head (preferably using the cat photo I have uploaded). Below you will find a picture of the rough sort of image I am hoping we can acheive but I am very open to suggestions. Title of book and authors name in striking shiney effect gold and or silver typeset. Book title larger font than the authors name. Glossy finish. Possibly part `ghosty` or cloudy imaging fading at the bottom/top?. Please ask me any questions you may find useful. Many thanks. Peter.

Target Market(s)

Family friendly fictional novel.

Font styles to use
Serif
Decorative

Colors
f04a50
f68d4c
ffcf3e
fbee3e

Requirements
Must have
• Something that catches the eye....
I bet you`ve never had that request before 8-)
Nice to have
• A rural canal scene, a lock where the boats come through to a different level of the water, a narrow-boat or two moored up at the side of the canal, some pretty rural scenery (Grass, Trees etc Summer or Autumn), A nice blue sky with a small amount of cloud or a stunning red sunset, a magpie, a stag that is not too noticeable in the distance but is visible once spotted. A photobomb of a black and white cats head taking up about 20% of the cover in the bottom corner, left hand side or right hand side will be dependant on cover design (preferably using my enclosed cat photo)
Nice large gold or silver shiny effect font.
many thanks P.
Should not have
• Busy town/city. Any boats other than a narrow-boat

```html
<!DOCTYPE html>
<html lang="en">
<head>
<meta charset="utf-8">
<title>Beneath the Quiet Copper Fern – Paperback Cover</title>
<link rel="stylesheet" href="https://fonts.googleapis.com/css2?family=Cinzel:wght@400&family=EB+Garamond:wght@400&family=Pinyon+Script&display=swap">
<style>
  :root {
    --back-dark: #140306;
    --back-mid: #22080c;
    --spine-edge: #4b3c3d;
    --ink: #0d0a0b;
    --paper: #ffffff;
    --body-text: #f3eeee;
    --sky-top: #aacbe0;
    --sky-low: #dbe9f1;
    --tree-green: #4f7a55;
    --tree-light: #8fb07a;
    --water: #5d6f7c;
    --water-dark: #1e2a33;
    --author: #f6f6f6;
  }
  * { margin: 0; padding: 0; box-sizing: border-box; }
  html, body { width: 1200px; height: 830px; overflow: hidden; background: var(--back-dark); }

  .cover-wrap {
    position: relative;
    width: 1200px;
    height: 830px;
    overflow: hidden;
    background: var(--back-dark);
  }

  /* Back cover */
  .back-cover {
    position: absolute;
    left: 0; top: 0;
    width: 560px; height: 830px;
    background: linear-gradient(90deg, var(--back-dark) 0%, var(--back-mid) 100%);
  }
  .blurb {
    position: absolute;
    left: 64px; top: 87px;
    width: 444px;
    font-family: "EB Garamond", Georgia, serif;
    font-size: 15.2px;
    line-height: 17.6px;
    color: var(--body-text);
    text-align: justify;
    hyphens: auto;
  }
  .blurb p + p { margin-top: 17.6px; }
  .isbn-box {
    position: absolute;
    left: 64px; top: 689px;
    width: 139px; height: 82px;
    background: var(--paper);
  }

  /* Spine */
  .spine {
    position: absolute;
    left: 560px; top: 0;
    width: 86px; height: 830px;
    background: linear-gradient(90deg, var(--back-mid) 0%, #2d1518 55%, var(--spine-edge) 100%);
  }
  .spine-title, .spine-author {
    position: absolute;
    writing-mode: vertical-rl;
    transform: rotate(180deg);
    color: var(--paper);
    white-space: nowrap;
  }
  .spine-title {
    left: 14px; top: 32px;
    height: 588px;
    font-family: "Cinzel", "Times New Roman", serif;
    font-size: 33px;
    text-align: start;
  }
  .spine-title .script {
    font-family: "Pinyon Script", cursive;
    font-size: 36px;
  }
  .spine-author {
    left: 31px; top: 640px;
    height: 170px;
    font-family: "Cinzel", "Times New Roman", serif;
    font-size: 10.5px;
    letter-spacing: 3px;
    text-align: center;
  }

  /* Front cover */
  .front-cover {
    position: absolute;
    left: 646px; top: 0;
    width: 554px; height: 830px;
  }
  .cover-photo {
    position: absolute;
    inset: 0;
    background:
      radial-gradient(ellipse 70% 22% at 55% 100%, rgba(8,10,14,0.9) 0%, rgba(8,10,14,0) 100%),
      linear-gradient(180deg,
        var(--sky-top) 0%,
        var(--sky-low) 22%,
        var(--tree-light) 32%,
        var(--tree-green) 45%,
        #3c5a44 55%,
        var(--water) 65%,
        #3e4d58 82%,
        var(--water-dark) 100%);
  }
  .cover-photo::before {
    content: "";
    position: absolute;
    inset: 0;
    background: linear-gradient(90deg, rgba(75,60,61,0.65) 0%, rgba(75,60,61,0) 12%);
  }

  .title-rule {
    position: absolute;
    left: 120px; top: 39px;
    width: 320px; height: 2px;
    background: var(--ink);
  }
  .cover-title {
    position: absolute;
    left: 0; top: 62px;
    width: 554px;
    text-align: center;
    color: var(--ink);
    font-weight: 400;
  }
  .cover-title .line-serif {
    display: block;
    font-family: "Cinzel", "Times New Roman", serif;
    font-size: 50px;
    line-height: 50px;
    margin-left: 20px;
  }
  .cover-title .line-script {
    display: block;
    font-family: "Pinyon Script", cursive;
    font-size: 82px;
    line-height: 96px;
    margin-left: 14px;
  }

  .cover-author {
    position: absolute;
    left: 0; top: 758px;
    width: 554px;
    text-align: center;
    white-space: nowrap;
    font-family: "Cinzel", "Times New Roman", serif;
    font-size: 30px;
    line-height: 36px;
    letter-spacing: 8px;
    color: var(--author);
    text-shadow: 0 0 6px rgba(0,0,0,0.6);
    padding-left: 30px;
  }
</style>
</head>
<body>
<div class="cover-wrap">

  <section class="back-cover">
    <div class="blurb">
      <p>Lorem ipsum dolor sit amet, consectetur adipiscing elit. Ut eget ante mollis, pulvinar dolor varius, placerat nulla. Ut gravida mollis dui eu pulvinar. Mauris tempor quam quam. Nulla leo nisi, congue ut ligula vel, faucibus tincidunt velit. Nulla fermentum magna convallis urna condimentum fermentum. Cras elementum pretium sem a maximus. Sed in odio vitae arcu maximus pellentesque. Pellentesque ut eleifend urna. Aenean in laoreet dolor, eu imperdiet tortor. Aenean bibendum ullamcorper dolor, vel vestibulum libero feugiat quis. Sed aliquam laoreet mauris ac finibus. Proin faucibus nunc eget tortor euismod tincidunt. Pellentesque semper efficitur massa, vel lobortis sapien pretium ac.</p>
      <p>Morbi ac metus nec mauris rutrum posuere vel at leo. Vestibulum porttitor, nulla at aliquet bibendum, est orci consequat arcu, sit amet interdum est ante vel dolor. Nunc placerat lectus et ligula hendrerit cursus. Praesent sed erat ullamcorper justo auctor ornare. In sodales dui facilisis semper placerat. Aenean risus sem, vulputate at orci at, semper euismod turpis. Curabitur fermentum ante quis purus dignissim, a tempus leo vehicula. Mauris eget lectus sollicitudin, tincidunt justo sed, sagittis leo. Phasellus erat ex, vestibulum ut rhoncus scelerisque, euismod at leo. Etiam id massa urna. Mauris eu euismod sapien. Nam non hendrerit augue, non congue diam.</p>
    </div>
    <div class="isbn-box"></div>
  </section>

  <section class="spine">
    <div class="spine-title">Beneath the Quiet <span class="script">Copper Fern</span></div>
    <div class="spine-author">Peter R Dunmore</div>
  </section>

  <section class="front-cover">
    <div class="cover-photo" role="img" aria-label="Photograph of a tree-lined canal under a pale blue sky, with a footbridge in the distance, a narrow-boat moored at the left bank, a magpie in flight and a black and white cat in the lower right corner"></div>
    <div class="title-rule"></div>
    <h1 class="cover-title">
      <span class="line-serif">Beneath</span>
      <span class="line-serif">the Quiet</span>
      <span class="line-script">Copper Fern</span>
    </h1>
    <div class="cover-author">Peter R Dunmore</div>
  </section>

</div>
</body>
</html>
```